Purchase Protection Subscription Program needs a refreshed website

We are refreshing an existing website www.carevaultplus.example. This is a purchase protection product which allows its members to receive extended warranty on the items they buy, receive a rebate of 50% on a repair of an item, a personal shopping concierge, etc. We are looking for a fresh, clean approach - with mass appeal to both men and woman. The site should convey trust, and ease of use.

Thanks to everyone who posted designs. Amazing work! It was a very difficult decision!

```html
<!DOCTYPE html>
<html lang="en">
<head>
<meta charset="utf-8">
<title>CareVault Plus</title>
<link href="https://fonts.googleapis.com/css2?family=Open+Sans:wght@400;600;700&display=swap" rel="stylesheet">
<style>
:root{
  --navy:#184766;
  --red:#a8162a;
  --page:#f4f5f7;
  --ink:#2b2b2b;
  --muted:#555;
  --footer:#2f3233;
  --footer-text:#c9c9c9;
  --base:#0d0d0d;
  --white:#fff;
}
*{margin:0;padding:0;box-sizing:border-box}
html,body{width:1070px;height:1200px;overflow:hidden}
body{position:relative;background:var(--page);font-family:"Open Sans",Arial,sans-serif;color:var(--ink)}
.abs{position:absolute}
.header{left:0;top:0;width:1070px;height:130px;background:var(--navy)}
.brand{left:152px;top:30px;font-size:27px;font-weight:400;color:var(--white);letter-spacing:-.3px}
.search{left:681px;top:32px;width:234px;height:27px;background:var(--white)}
.search svg{position:absolute;right:8px;top:6px}
.nav{left:152px;top:104px;display:flex;gap:30px;font-size:11px;color:var(--white);text-transform:uppercase}
.nav .active{position:relative}
.nav .active::after{content:"";position:absolute;left:50%;top:19px;margin-left:-7px;border:7px solid transparent;border-bottom-color:var(--page);border-top:0}
.profile{left:734px;top:104px;font-size:11px;color:var(--white)}
.login{left:861px;top:98px;width:54px;height:25px;background:var(--red);color:var(--white);font-size:11px;text-align:center;line-height:25px}
.hero-band{left:154px;top:161px;width:761px;height:272px;background:var(--red)}
.hero-photo{left:154px;top:161px;width:527px;height:251px;background:linear-gradient(120deg,#6b6460,#c8bfb6 45%,#e8e6e3 75%,#9a8d80)}
.hero-copy{left:695px;top:193px;width:206px;color:#f3d9dc;font-size:10.5px;line-height:14.2px;text-align:justify}
.hero-copy h1{color:var(--white);font-size:18px;font-weight:700;margin-bottom:12px;letter-spacing:.2px}
.hero-copy p+p{margin-top:14px}
.dots{left:696px;top:404px;display:flex;gap:8px}
.dots span{width:9px;height:9px;background:var(--white)}
.card-photo{top:464px;width:234px;height:143px}
.card-title{top:622px;font-size:14px;color:var(--ink)}
.card-text{top:652px;width:234px;font-size:10.5px;line-height:14.3px;text-align:justify;color:var(--ink)}
.list{list-style:none;margin-top:12px}
.list li{display:flex;align-items:center;gap:11px;margin-bottom:5px}
.rule{top:757px;width:234px;height:1px;background:#333}
.more{top:740px;width:48px;height:18px;background:#333;color:var(--white);font-size:10px;text-align:center;line-height:18px}
.sec-head{top:785px;height:31px;color:var(--white);font-size:12.5px;font-weight:700;line-height:31px;padding-left:17px}
.about-text{left:153px;top:840px;width:234px;font-size:10.5px;line-height:14.3px;text-align:justify}
.about-text p{margin-bottom:14px}
.feature-photo{top:844px;width:145px;height:95px}
.feature-title{top:954px;font-size:11.5px;text-transform:uppercase}
.feature-text{top:977px;width:145px;font-size:9.5px;line-height:11.5px;text-align:justify}
.line-end{height:1px}
.line-end::after{content:"";position:absolute;right:0;top:-4px;width:9px;height:9px}
.footer{left:0;top:1038px;width:1070px;height:128px;background:var(--footer)}
.fcol{top:1052px;font-size:9.5px;line-height:14.3px;color:var(--footer-text)}
.fcol h3{font-size:10.5px;font-weight:400;color:var(--white);margin-bottom:9px}
.fcol b{color:var(--white);font-weight:600}
.sub-input{left:747px;top:1127px;width:117px;height:17px;background:#eee}
.sub-btn{left:864px;top:1127px;width:54px;height:17px;background:var(--navy);color:var(--white);font-size:8px;text-align:center;line-height:17px}
.base{left:0;top:1166px;width:1070px;height:34px;background:var(--base);color:#aaa;font-size:9px;text-align:center;line-height:34px}
</style>
</head>
<body>
<header class="abs header"></header>
<div class="abs brand">CareVault Plus</div>
<div class="abs search"><svg width="16" height="14" viewBox="0 0 16 14"><circle cx="6" cy="5.5" r="4" fill="none" stroke="#222" stroke-width="2"/><line x1="9" y1="8.5" x2="14" y2="12.5" stroke="#222" stroke-width="2.5"/></svg></div>
<nav class="abs nav"><span class="active">Home</span><span>About us</span><span>Services</span><span>Product features</span><span>How it works</span><span>Contact us</span></nav>
<div class="abs profile">MANAGE USER PROFILE</div>
<div class="abs login">LOGIN</div>

<div class="abs hero-band"></div>
<div class="abs hero-photo" role="img" aria-label="Three colleagues reviewing documents together in an office"></div>
<div class="abs hero-copy">
  <h1>CareVault Plus</h1>
  <p>Lorem Ipsum is simply dummy text of the printing and typesetting industry. Lorem Ipsum has been the industry's standard dummy text ever since the 1500s securely online. Then download what you need and submit your claim online.securely online.</p>
  <p>Lorem Ipsum is simply dummy text of the printing and typesetting industry. Lorem Ipsum has been the industry's standard dummy text ever since the 1500s</p>
</div>
<div class="abs dots"><span></span><span></span><span></span><span></span></div>

<div class="abs card-photo" style="left:154px;background:linear-gradient(135deg,#5b4f50,#b9a6a2 55%,#6d6567)" role="img" aria-label="Hand holding a set of house keys"></div>
<div class="abs card-photo" style="left:418px;background:linear-gradient(160deg,#2b2b2b 35%,#8b8b86 55%,#e9e9e6 80%)" role="img" aria-label="Hands at a laptop beside paperwork and a pen"></div>
<div class="abs card-photo" style="left:681px;background:linear-gradient(135deg,#6c5a3e,#b79a6b 45%,#8ea0c2 70%,#4c4a44)" role="img" aria-label="Hand inserting a card into a payment terminal"></div>

<div class="abs card-title" style="left:154px">Valuable purchase protection</div>
<div class="abs card-title" style="left:419px">Easy claims process</div>
<div class="abs card-title" style="left:681px">One low monthly fee</div>

<div class="abs card-text" style="left:153px">
  <p>GET 5 UNIQUE WAYS TO GET MORE OUT OF THE THINGS YOU BUY:*</p>
  <ul class="list">
    <li><svg width="11" height="11"><rect width="11" height="11" fill="#a8162a"/><path d="M4 2.5 8 5.5 4 8.5Z" fill="#fff"/></svg>Warranty extension</li>
    <li><svg width="11" height="11"><rect width="11" height="11" fill="#a8162a"/><path d="M4 2.5 8 5.5 4 8.5Z" fill="#fff"/></svg>Repair bill rebate</li>
  </ul>
</div>
<div class="abs card-text" style="left:418px">Using CareVault Plus has never been easier. Just send us copies, scans or photos of your receipts — we'll store them securely online. Then download what you need and submit your claim online.</div>
<div class="abs card-text" style="left:681px">Lorem Ipsum is simply dummy text of the printing and typesetting industry. Lorem Ipsum has been the industry's standard dummy text ever since the 1500s securely online. Then download what you need and submit your claim online.securely online.</div>

<div class="abs rule" style="left:154px"></div><div class="abs more" style="left:337px">More</div>
<div class="abs rule" style="left:419px"></div><div class="abs more" style="left:603px">More</div>
<div class="abs rule" style="left:683px"></div><div class="abs more" style="left:866px">More</div>

<div class="abs sec-head" style="left:153px;width:233px;background:var(--red)">ABOUT US</div>
<div class="abs sec-head" style="left:417px;width:498px;background:var(--navy);border-bottom:2px solid #0f3a55">Product Features</div>

<div class="abs about-text">
  <p>LOREM IPSUM DOLOR SIT AMET, CONSEC TETUER ADIPI SCINGSA ESSLIT. PRAESENT VESTIBULUM MOLESTIE LACUS. AENEAN NONUMMY HEDYATER HENDRERIT.</p>
  <p>Phasellus porta. Fusce suscipit varius mi. Cum sociis natoque penatibus et magnis dis parturi-</p>
  <p>ontes, nascetur ridiculus mus. Nulla dui. Fusce feugiat malesuada odio. Morbi nuncae-</p>
</div>
<div class="abs line-end" style="left:154px;top:1019px;width:233px;background:var(--red)"></div>
<div class="abs" style="left:378px;top:1014px;width:9px;height:9px;background:var(--red)"></div>

<div class="abs feature-photo" style="left:417px;background:linear-gradient(135deg,#dfe6ec,#5d6b7c 50%,#eef1f4)" role="img" aria-label="Businessman holding a tablet with colleagues behind"></div>
<div class="abs feature-photo" style="left:594px;background:linear-gradient(135deg,#e8ecf0,#4f5a68 50%,#cdd5de)" role="img" aria-label="Business team meeting around a table"></div>
<div class="abs feature-photo" style="left:771px;background:linear-gradient(135deg,#3a3e44,#a8b0b8 45%,#2f3338)" role="img" aria-label="Colleagues discussing work at a laptop"></div>

<div class="abs feature-title" style="left:417px">Experience</div>
<div class="abs feature-title" style="left:594px">Marketing</div>
<div class="abs feature-title" style="left:771px">Management</div>
<div class="abs feature-text" style="left:594px">isl vel nisi fringilla dapibus. Proin a felis massa. Maecenas iaculis eros in lorem</div>
<div class="abs feature-text" style="left:417px">isl vel nisi fringilla dapibus. Proin a felis massa. Maecenas iaculis eros in lorem</div>
<div class="abs feature-text" style="left:771px">isl vel nisi fringilla dapibus. Proin a felis massa. Maecenas iaculis eros in lorem</div>

<div class="abs" style="left:417px;top:1019px;width:145px;height:1px;background:var(--navy)"></div>
<div class="abs" style="left:553px;top:1011px;width:9px;height:9px;background:var(--navy)"></div>
<div class="abs" style="left:594px;top:1019px;width:145px;height:1px;background:var(--navy)"></div>
<div class="abs" style="left:730px;top:1011px;width:9px;height:9px;background:var(--navy)"></div>
<div class="abs" style="left:771px;top:1019px;width:145px;height:1px;background:var(--navy)"></div>
<div class="abs" style="left:907px;top:1011px;width:9px;height:9px;background:var(--navy)"></div>

<footer class="abs footer"></footer>
<div class="abs fcol" style="left:153px;width:200px">
  <h3>CONTACT INFO</h3>
  <p><b>Address:</b> Company Inc., 4120<br>Alder Lane, Leeds, L09</p>
  <p style="margin-top:5px"><b>Telephone:</b> 800 555 0142</p>
  <p style="margin-top:5px"><b>Email:</b>contact@carevaultplus.example</p>
</div>
<div class="abs fcol" style="left:391px">
  <h3>EXPLORE</h3>
  <p>Product Features</p><p>Privacy</p><p>How it works</p><p>About Us</p><p>Valuable purchase</p>
</div>
<div class="abs fcol" style="left:576px">
  <h3>FOLLOW US</h3>
  <p>Friendspace</p><p>Chirpline</p><p>Workgrid</p><p>Clipstream</p><p>Blog</p>
</div>
<div class="abs fcol" style="left:747px;width:180px">
  <h3>STAY CONNECTED</h3>
  <p>Allways stay updated</p>
  <p>Subscribe and stay up to date with the latest news from us</p>
</div>
<div class="abs sub-input"></div>
<div class="abs sub-btn">SUBSCIBE</div>
<div class="abs base">CareVaultPlus© 2014</div>
</body>
</html>
```